Web Design Project

Looking for a web page design for a consulting company called Tembeka Consulting.

Tembeka specialize in Business Improvement and Transformation consulting in the Mining, Infrastructure, Logistics and Transport sectors.

Industry/Entity Type

Business

Font styles to use
Sans Serif

Colors
86cae7
0892cd
ecf7f5

```html
<!DOCTYPE html>
<html lang="en">
<head>
<meta charset="utf-8">
<title>Tembeka Consulting</title>
<link rel="stylesheet" href="https://fonts.googleapis.com/css2?family=Cinzel:wght@400;700&family=Open+Sans:wght@400;600;700&display=swap">
<style>
  :root {
    --blue: #0892cd;
    --blue-mid: #2a9fd6;
    --blue-light: #86cae7;
    --mint: #ecf7f5;
    --ink: #333;
    --ink-soft: #555;
    --rule: #c9c9c9;
    --card-border: #cfcfcf;
    --btn: #7a7a7a;
    --white: #fff;
  }
  * { box-sizing: border-box; margin: 0; padding: 0; }
  html, body { width: 903px; height: 1200px; overflow: hidden; background: var(--white); }
  body { position: relative; font-family: "Open Sans", Arial, sans-serif; color: var(--ink); }
  .abs { position: absolute; }

  /* header */
  .brand { left: 18px; top: 30px; width: 120px; text-align: center; }
  .brand-mark { width: 26px; height: 26px; border-radius: 50%; background: var(--blue-mid); margin: 0 auto 10px; }
  .brand-name { font-family: "Cinzel", serif; font-size: 20px; letter-spacing: 3px; color: var(--ink-soft); line-height: 1.1; }
  .brand-sub { font-family: "Cinzel", serif; font-size: 9px; letter-spacing: 3px; color: var(--ink-soft); line-height: 1.1; }

  .nav { left: 0; top: 0; width: 903px; height: 117px; list-style: none; }
  .nav li { position: absolute; top: 94px; font-family: "Cinzel", serif; font-size: 12px; letter-spacing: .3px;
    color: #444; white-space: nowrap; line-height: 14px; }
  .nav-active { position: absolute; left: 270px; top: 0; width: 82px; height: 117px; background: var(--blue-mid); }
  .nav li.active { left: 270px; width: 82px; text-align: center; color: var(--white); }

  .hero { left: 11px; top: 131px; width: 881px; height: 390px;
    background: linear-gradient(90deg, #7fb4cc 0%, #b8d6e4 30%, #dfeaf0 55%, #9fc2d6 80%, #c8dce8 100%); }

  /* service cards */
  .card { top: 545px; width: 211px; height: 276px; border: 1px solid var(--card-border); background: var(--white); text-align: center; }
  .card-art { position: absolute; left: 22px; top: 12px; width: 167px; height: 128px; border-radius: 6px;
    background: radial-gradient(ellipse at center, #f3d35a 0%, #e9e9e9 70%, #fff 100%); }
  .card-art.orange { background: radial-gradient(ellipse at center, #f07b3a 0%, #ebebeb 70%, #fff 100%); }
  .card-title { position: absolute; left: 0; right: 0; top: 154px; font-family: "Cinzel", serif; font-weight: 400;
    font-size: 18px; line-height: 22px; color: var(--blue); letter-spacing: .3px; white-space: nowrap; }
  .card-text { position: absolute; left: 14px; right: 14px; top: 189px; font-size: 11px; line-height: 11px; color: var(--ink-soft); }
  .card-btn { position: absolute; left: 55px; top: 233px; width: 84px; height: 28px; background: var(--btn); border-radius: 3px;
    color: var(--white); font-size: 12px; font-weight: 700; font-style: italic; line-height: 28px; }
  .rule { height: 1px; background: var(--rule); }

  /* lower sections */
  .section-title { font-family: "Cinzel", serif; font-weight: 400; font-size: 22px; line-height: 26px; color: #444; letter-spacing: .8px; white-space: nowrap; }
  .quote { left: 20px; width: 300px; font-size: 13.5px; line-height: 15.5px; color: #444; padding-left: 31px; }
  .quote-mark { position: absolute; left: 0; top: 2px; }
  .quote-author { color: var(--blue); font-weight: 600; }
  .about-photo { left: 374px; top: 887px; width: 256px; height: 173px;
    background: linear-gradient(120deg, #d8dde2 0%, #b9c2cb 45%, #e9ece9 100%); }
  .about-text { font-size: 13.5px; line-height: 15.6px; color: #444; }

  .footer-left, .footer-nav { top: 1163px; font-size: 12px; color: var(--ink-soft); white-space: nowrap; }
  .footer-nav span.dot { margin: 0 5px; }
</style>
</head>
<body>

<header>
  <div class="abs brand">
    <div class="brand-mark"></div>
    <div class="brand-name">TEMBEKA</div>
    <div class="brand-sub">CONSULTING</div>
  </div>
  <div class="nav-active"></div>
  <ul class="abs nav">
    <li class="active">HOME</li>
    <li style="left:375px">ABOUT US</li>
    <li style="left:481px">SERVICES</li>
    <li style="left:581px">TESTIMONIALS</li>
    <li style="left:715px">NEWS</li>
    <li style="left:794px">CONTACT US</li>
  </ul>
</header>

<div class="abs hero" role="img" aria-label="Photo of four smiling business people shaking hands in a glass office"></div>

<section class="services">
  <div class="abs card" style="left:15px">
    <div class="card-art" role="img" aria-label="Illustration of a yellow bulldozer"></div>
    <h3 class="card-title">MINING</h3>
    <p class="card-text">Lorem ipsum dolor sit amet, consectetuer adipiscing elit, sed diam nonummy nibh euismod</p>
    <div class="card-btn">MORE</div>
  </div>
  <div class="abs card" style="left:236px">
    <div class="card-art orange" role="img" aria-label="Illustration of an orange dump truck unloading sand"></div>
    <h3 class="card-title">INFRASTRUCTURE</h3>
    <p class="card-text">Lorem ipsum dolor sit amet, consectetuer adipiscing elit, sed diam nonummy nibh euismod</p>
    <div class="card-btn">MORE</div>
  </div>
  <div class="abs card" style="left:456px">
    <div class="card-art" role="img" aria-label="Illustration of a yellow wheel loader"></div>
    <h3 class="card-title">LOGISTICS</h3>
    <p class="card-text">Lorem ipsum dolor sit amet, consectetuer adipiscing elit, sed diam nonummy nibh euismod</p>
    <div class="card-btn">MORE</div>
  </div>
  <div class="abs card" style="left:676px">
    <div class="card-art orange" role="img" aria-label="Illustration of an orange truck carrying bricks"></div>
    <h3 class="card-title">TRANSPORTATION</h3>
    <p class="card-text">Lorem ipsum dolor sit amet, consectetuer adipiscing elit, sed diam nonummy nibh euismod</p>
    <div class="card-btn">MORE</div>
  </div>
  <div class="abs rule" style="left:15px; top:823px; width:872px"></div>
</section>

<section class="testimonials">
  <h2 class="abs section-title" style="left:18px; top:848px">TESTIMONIALS</h2>
  <div class="abs quote" style="top:889px">
    <svg class="quote-mark" width="22" height="12" viewBox="0 0 22 12"><path d="M3 0h6L6 12H0zM14 0h6l-3 12h-6z" fill="var(--blue-light)"/></svg>
    Lorem ipsum dolor sit amet, consec tetuer adipiscing. Praesent vestibu lum molestie lacuiirhs. Aenean non ummy hendreriauris. Phasellllus.<br>
    <span class="quote-author">Rosalind K.</span>
  </div>
  <div class="abs quote" style="top:1010px">
    <svg class="quote-mark" width="22" height="12" viewBox="0 0 22 12"><path d="M3 0h6L6 12H0zM14 0h6l-3 12h-6z" fill="var(--blue-light)"/></svg>
    Duis autem vel eum iriure dolor in hendrerit in vulputate velit esse molestie consequat, vel illum dolore eu feugiat nulla facilisis at vero eros et accumsan.<br>
    <span class="quote-author">Darius P.</span>
  </div>
</section>

<section class="about">
  <h2 class="abs section-title" style="left:375px; top:848px">ABOUT TEMBEKA CONSULTING</h2>
  <div class="abs about-photo" role="img" aria-label="Photo of three colleagues reviewing documents together"></div>
  <p class="abs about-text" style="left:643px; top:886px; width:236px">Typi non habent claritatem insitam; est usus legentis in iis qui facit eorum claritatem. Investigationes demonstraverunt lectores legere me lius quod ii legunt saepius. Claritas est etiam processus dynamicus, qui sequitur mutationem consuetudium lectorum. Mirum est notare quam littera gothica, quam nunc putamus parum claram, anteposuerit litterarum formas humanitatis per</p>
  <p class="abs about-text" style="left:372px; top:1072px; width:515px">seacula quarta decima et quinta decima. Eodem modo typi, qui nunc nobis videntur parum clari, fiant sollemnes in futurum.</p>
</section>

<footer>
  <div class="abs rule" style="left:14px; top:1147px; width:874px; background:#999"></div>
  <div class="abs footer-left" style="left:18px">2013 © Privacy Policy</div>
  <div class="abs footer-nav" style="right:17px">Home<span class="dot">·</span>About Us<span class="dot">·</span>Services<span class="dot">·</span>Testimonials<span class="dot">·</span>News<span class="dot">·</span>Contact Us</div>
</footer>

</body>
</html>
```